Salve Label

2.25 inch round label.

We are looking for a simple label, muted natural colors, sophisticated, elegant, calming.

Name of Product: Herbal Beeswax Salve
This scent is lavender - but there will be others scents
Want this label to be adaptable to other scents with simple color and word changes.

Other things to express on the label - all natural, calming, relaxing

Name of the Company: Tansy Ridge Farm
2 oz.

```html
<!DOCTYPE html>
<html lang="en">
<head>
<meta charset="utf-8">
<title>Herbal Beeswax Salve – Lavender Label</title>
<link href="https://fonts.googleapis.com/css2?family=Montserrat:wght@400;500;600&family=Oswald:wght@600&display=swap" rel="stylesheet">
<style>
  :root {
    --backdrop: #e4e1dd;
    --label-white: #ededee;
    --scent: #a59bb0;
    --scent-line: #a99fb5;
    --scent-text: #f4f2f6;
    --ink: #141414;
    --farm: #2f7d4a;
  }
  html, body {
    margin: 0;
    padding: 0;
    width: 1047px;
    height: 1200px;
    overflow: hidden;
    background: var(--backdrop);
  }
  .salve-label {
    display: block;
    width: 1047px;
    height: 1200px;
  }
  .label-face { fill: var(--label-white); }
  .outer-ring, .inner-ring { fill: none; stroke: var(--scent-line); }
  .outer-ring { stroke-width: 5; }
  .inner-ring { stroke-width: 4; }
  .side-hatch { fill: none; stroke: var(--scent-line); stroke-width: 14; stroke-dasharray: 2 5; }
  .side-rule { fill: none; stroke: var(--scent-line); stroke-width: 4; }
  .benefits {
    font-family: 'Montserrat', sans-serif;
    font-weight: 500;
    font-size: 40px;
    letter-spacing: 5px;
    fill: var(--scent);
  }
  .farm-name {
    font-family: 'Montserrat', sans-serif;
    font-weight: 600;
    font-size: 54px;
    fill: var(--farm);
  }
  .scent-band { fill: var(--scent); }
  .product-name {
    font-family: 'Oswald', sans-serif;
    font-weight: 600;
    font-size: 70px;
    letter-spacing: 1px;
    fill: var(--ink);
  }
  .scent-name {
    font-family: 'Montserrat', sans-serif;
    font-weight: 500;
    font-size: 74px;
    letter-spacing: 2px;
    fill: var(--scent-text);
  }
  .net-weight {
    font-family: 'Montserrat', sans-serif;
    font-weight: 500;
    font-size: 32px;
    fill: var(--ink);
  }
</style>
</head>
<body>
<svg class="salve-label" viewBox="0 0 1047 1200" xmlns="http://www.w3.org/2000/svg">
  <defs>
    <clipPath id="inner-area">
      <circle cx="523.5" cy="600" r="368"/>
    </clipPath>
    <path id="benefit-arc" d="M 123.5 600 A 400 400 0 0 1 923.5 600"/>
  </defs>

  <circle class="label-face" cx="523.5" cy="600" r="455"/>
  <circle class="outer-ring" cx="523.5" cy="600" r="435"/>
  <circle class="inner-ring" cx="523.5" cy="600" r="370"/>

  <!-- side rules -->
  <path class="side-hatch" d="M 125.2 635 A 400 400 0 0 0 160 760"/>
  <path class="side-hatch" d="M 921.8 635 A 400 400 0 0 1 887 760"/>
  <path class="side-rule" d="M 168 775 A 400 400 0 0 0 240 880"/>
  <path class="side-rule" d="M 879 775 A 400 400 0 0 1 807 880"/>

  <text class="benefits" text-anchor="middle">
    <textPath href="#benefit-arc" startOffset="50%">ALL NATURAL - CALMING - RELAXING</textPath>
  </text>

  <text class="farm-name" x="523.5" y="520" text-anchor="middle">Tansy Ridge Farm</text>

  <g clip-path="url(#inner-area)">
    <rect class="scent-band" x="150" y="690" width="750" height="200" role="img" aria-label="Lavender band with soft honeycomb texture"/>
  </g>

  <text class="product-name" x="523.5" y="668" text-anchor="middle">HERBAL BEESWAX SALVE</text>
  <text class="scent-name" x="523.5" y="812" text-anchor="middle">LAVENDER</text>
  <text class="net-weight" x="523.5" y="940" text-anchor="middle">Net Wt: 2 oz</text>
</svg>
</body>
</html>
```